Business card required for IT Consultancy Business - Bluefern Consulting.
Company provides the whole nine yards of services across IT Architecture, design and execution.
Basically we provide consulting services to help businesses make sure their technology is enabling their business strategy.
Design for front and back required.
We would like the front of the card to inlcude:
Name
Title
Mobile number
email address
www.BFQ.com.au
Company logos attached.
Thank you
Industry/Entity Type
Business
Contact Information for Business Card
Name
Title
Mobile number
email address
www.BFQ.com.au
Look and feel
Each slider illustrates characteristics of the customer's brand and the style your logo design should communicate.

```html
<!DOCTYPE html>
<html lang="en">
<head>
<meta charset="utf-8">
<title>Bluefern Consulting – Business Card</title>
<link href="https://fonts.googleapis.com/css2?family=Roboto+Condensed:wght@700&family=Roboto:wght@400;500&display=swap" rel="stylesheet">
<style>
  :root {
    --backdrop: #2b2b2d;
    --card-light: #f7f7f7;
    --card-dark: #262728;
    --brand-blue: #1e7fd0;
    --brand-orange: #f0531f;
    --ink-grey: #555658;
    --text-light: #f2f2f2;
    --divider: #8a8b8d;
  }
  * { margin: 0; padding: 0; box-sizing: border-box; }
  html, body {
    width: 1200px; height: 900px; overflow: hidden;
    background: var(--backdrop);
  }
  .stage {
    position: relative; width: 1200px; height: 900px;
    display: flex; flex-direction: column; align-items: center; justify-content: center; gap: 40px;
  }
  .card {
    width: 660px; height: 377px; position: relative;
    box-shadow: 0 14px 30px rgba(0,0,0,0.45);
  }
  .card--front {
    background: var(--card-light);
    display: flex; flex-direction: column; align-items: center; justify-content: center;
  }
  .brand {
    display: flex; align-items: center; gap: 14px; margin-top: -10px;
  }
  .brand__dot {
    width: 34px; height: 34px; border-radius: 50%; background: var(--brand-orange);
  }
  .brand__name {
    font-family: "Roboto Condensed", sans-serif; font-weight: 700;
    font-size: 46px; color: var(--brand-blue); letter-spacing: 0.5px;
  }
  .front__url {
    position: absolute; bottom: 52px; left: 0; right: 0; text-align: center;
    font-family: "Roboto", sans-serif; font-weight: 400;
    font-size: 15px; letter-spacing: 9px; color: var(--ink-grey);
  }
  .card--back {
    background: var(--card-dark);
    display: flex; align-items: center; justify-content: center; gap: 30px;
  }
  .person { text-align: right; }
  .person__name {
    font-family: "Roboto Condensed", sans-serif; font-weight: 700;
    font-size: 36px; color: var(--brand-blue); line-height: 1.05;
  }
  .person__title {
    font-family: "Roboto Condensed", sans-serif; font-weight: 700;
    font-size: 19px; color: var(--brand-orange); margin-top: 4px;
  }
  .divider { width: 2px; height: 92px; background: var(--divider); }
  .contacts { list-style: none; display: flex; flex-direction: column; gap: 6px; }
  .contacts__item {
    display: flex; align-items: center; gap: 10px;
    font-family: "Roboto", sans-serif; font-weight: 500;
    font-size: 18px; color: var(--text-light);
  }
  .contacts__icon { width: 16px; height: 16px; flex: none; }
</style>
</head>
<body>
<main class="stage">
  <section class="card card--front">
    <div class="brand">
      <span class="brand__dot"></span>
      <span class="brand__name">Bluefern Consulting</span>
    </div>
    <p class="front__url">www.BFQ.com.au</p>
  </section>

  <section class="card card--back">
    <div class="person">
      <h1 class="person__name">DANIEL REYES</h1>
      <p class="person__title">CEO/FOUNDER</p>
    </div>
    <span class="divider"></span>
    <ul class="contacts">
      <li class="contacts__item">
        <svg class="contacts__icon" viewBox="0 0 16 16" aria-hidden="true">
          <rect x="4" y="1" width="8" height="14" rx="1.5" fill="none" stroke="#1e7fd0" stroke-width="1.6"/>
          <circle cx="8" cy="12.5" r="0.9" fill="#1e7fd0"/>
        </svg>
        555 214 7083
      </li>
      <li class="contacts__item">
        <svg class="contacts__icon" viewBox="0 0 16 16" aria-hidden="true">
          <rect x="1" y="3" width="14" height="10" fill="#1e7fd0"/>
          <path d="M1 3 L8 9 L15 3" fill="none" stroke="#262728" stroke-width="1.3"/>
        </svg>
        hello@bluefern.com
      </li>
      <li class="contacts__item">
        <svg class="contacts__icon" viewBox="0 0 16 16" aria-hidden="true">
          <circle cx="8" cy="8" r="7" fill="#1e7fd0"/>
          <path d="M1 8 H15 M8 1 C4 5 4 11 8 15 M8 1 C12 5 12 11 8 15" fill="none" stroke="#262728" stroke-width="1"/>
        </svg>
        www.BFQ.com.au
      </li>
    </ul>
  </section>
</main>
</body>
</html>
```